ReDesign Website for a more Bold approach

Hello! I'd like to redesign my website: holvencrest.com

I'd like to add one thing that's not on my website which is a blog. The design around the blog should be put time into as I will be putting out incredibly great content and want it to attract viewers.

I get a lot of inspiration from ruvtal.com (the way they flow the big statements across each screen, colors)
moorlane.vc (the simplicity behind the design is beautiful)

I like modern very simple but bold approaches.

I am going to attach my logo here and if it can be thought of when making the design of the website. Thanks!

Industry/Entity Type

Finance and Private Equity

Number of Pages Required

3 page

Font styles to use
Serif
Sans Serif

Colors
0054AA
0677BA
7BADD7
CADEEF
E8F1F8
0094D4
00A9DD
6FCCEA
C7EBF8
E9F6FB
00AB8E
00BBA5
67D7C9
C6EFE9
E9F9F6

Requirements
Must have
• My project must have a Home, Expertise, Story, Clients, Approach, Blog, Contact
Nice to have
• It would be nice to have these tabs reduced to 1-3 pages
Should not have
• My project must not have bright colors.

```html
<!DOCTYPE html>
<html lang="en">
<head>
<meta charset="utf-8">
<title>Holvencrest Ventures</title>
<link href="https://fonts.googleapis.com/css2?family=Poppins:wght@300;400;500;600;700&display=swap" rel="stylesheet">
<style>
:root{
  --navy:#1c2a48;
  --navy-2:#243556;
  --accent:#0054aa;
  --accent-2:#0677ba;
  --accent-soft:#7badd7;
  --ice:#e8f1f8;
  --ice-2:#cadeef;
  --ink:#1d2b4a;
  --muted:#5c6478;
  --line:#dfe3ea;
  --white:#ffffff;
}
*{margin:0;padding:0;box-sizing:border-box}
html,body{width:1200px;height:4858px;overflow:hidden}
body{position:relative;font-family:'Poppins',sans-serif;color:var(--ink);background:var(--white)}
.abs{position:absolute}
.photo{position:absolute}
.deco{position:absolute;border-radius:50%}
/* header */
.brand-box{left:0;top:0;width:321px;height:81px;background:var(--navy);display:flex;align-items:center;padding-left:26px;font-weight:700;font-size:21px;color:var(--white);letter-spacing:.3px;white-space:nowrap}
.brand-box span,.foot-brand span{color:var(--accent-soft)}
.nav{top:31px;left:577px;display:flex;gap:29px;font-size:12.5px;font-weight:500;color:var(--ink)}
.nav .active{color:var(--accent)}
/* hero */
.hero{left:0;top:81px;width:1200px;height:755px;background:var(--ice)}
.kicker{top:203px;width:1200px;text-align:center;font-size:17px;font-weight:300}
.headline{top:240px;width:1200px;text-align:center;font-size:64px;font-weight:300;line-height:81px;color:var(--navy)}
.btn-accent{left:515px;top:426px;width:170px;height:48px;background:var(--accent);color:var(--white);font-size:12px;font-weight:600;display:flex;align-items:center;justify-content:center}
.slider-dots{left:1148px;top:318px}
.hero-rule{left:89px;top:585px;width:1022px;height:1px;background:#cdd7e2}
.stat{top:640px}
.stat b{display:block;font-size:30px;font-weight:300;color:var(--navy)}
.stat small{display:block;font-size:10px;color:#7d8597;font-weight:500;margin-top:4px}
/* expertise */
.sec-title{font-size:46px;font-weight:300;color:var(--navy)}
.underline{height:2px;width:46px;background:#cfd5de}
.lead{font-size:15px;line-height:24px;color:var(--muted);text-align:center}
.skill{width:200px}
.skill h4{font-size:11.5px;font-weight:600;line-height:15px;color:var(--navy)}
.skill p{font-size:12.5px;line-height:20px;color:var(--muted);margin-top:10px}
/* story */
.story{left:232px;top:1680px;width:968px;height:618px;background:var(--accent)}
.story-copy{left:617px;top:1780px;width:495px;color:var(--white)}
.story-copy h2{font-size:44px;font-weight:300}
.story-copy p{font-size:12.5px;line-height:20.5px;margin-top:18px}
.btn-white{left:619px;top:2138px;width:207px;height:43px;background:var(--white);color:var(--navy);font-size:11.5px;font-weight:600;display:flex;align-items:center;justify-content:center}
/* portfolio */
.grid{left:89px;top:2495px;width:1022px;height:339px;display:grid;grid-template-columns:repeat(5,1fr);grid-template-rows:1fr 1fr}
.grid div{display:flex;align-items:center;justify-content:center;font-size:25px;font-weight:500;color:#3b4352;border-right:1px solid var(--line);border-bottom:1px solid var(--line)}
.grid div:nth-child(5n){border-right:none}
.grid div:nth-child(n+6){border-bottom:none}
/* approach */
.approach-bg{left:0;top:2972px;width:896px;height:619px;background:var(--ice)}
.approach-copy{left:89px;top:3066px;width:490px}
.approach-copy h2{font-size:46px;font-weight:300;color:var(--navy)}
.approach-copy p{font-size:12.5px;line-height:20.5px;color:var(--muted);margin-top:17px}
/* blog */
.card{top:3776px;width:279px;height:407px;background:var(--white);box-shadow:0 14px 34px rgba(28,42,72,.09)}
.card .thumb{height:236px}
.card .body{padding:26px 26px 0}
.card time{font-size:10.5px;color:var(--accent-2)}
.card h3{font-size:15px;font-weight:600;line-height:22px;margin-top:8px;color:var(--navy)}
.card p{font-size:12.5px;line-height:19px;color:var(--muted);margin-top:12px}
/* footer */
.footer{left:0;top:4291px;width:1200px;height:567px;background:var(--navy)}
.foot-brand{left:181px;top:4503px;font-size:29px;font-weight:600;color:var(--white);white-space:nowrap}
.social{top:4556px;width:56px;height:56px;border-radius:50%;background:var(--navy-2);border:1px solid #34476c}
.form-title{left:581px;top:4352px;font-size:26px;font-weight:300;color:var(--white)}
.label{font-size:9.5px;font-weight:600;color:var(--white)}
.field{background:var(--navy-2);border:1px solid #2d4066;color:#aab4c8;font-size:11px;padding:0 18px;display:flex;align-items:center}
.submit{left:583px;top:4706px;width:464px;height:40px;background:var(--accent);color:var(--white);font-size:12px;font-weight:600;display:flex;align-items:center;justify-content:center}
.foot-rule{left:89px;top:4804px;width:1022px;height:1px;background:#34476c}
.copyright{top:4823px;width:1200px;text-align:center;font-size:10.5px;color:var(--white)}
.to-top{left:1135px;top:4784px;width:40px;height:40px;border-radius:50%;background:var(--white)}
</style>
</head>
<body>

<!-- header -->
<div class="abs brand-box">HOLVENCREST&nbsp;<span>VENTURES</span></div>
<nav class="abs nav">
  <span class="active">HOME</span><span>EXPERTISE</span><span>STORY</span><span>CLIENTS</span><span>APPROACH</span><span>BLOG</span><span>CONTACT</span>
</nav>

<!-- hero -->
<section class="abs hero"></section>
<p class="abs kicker">Finance and Private Equity</p>
<h1 class="abs headline">Built by founders<br>for founders</h1>
<div class="deco" style="left:830px;top:195px;width:180px;height:180px;background:var(--ice-2);opacity:.45" role="img" aria-label="Soft decorative circle"></div>
<div class="abs btn-accent">FIND OUT MORE</div>
<svg class="abs slider-dots" width="14" height="50">
  <circle cx="7" cy="7" r="4.5" fill="none" stroke="#1c2a48" stroke-width="2"/>
  <circle cx="7" cy="25" r="4.5" fill="none" stroke="#9aa3b3" stroke-width="1.5"/>
  <circle cx="7" cy="43" r="4.5" fill="none" stroke="#1c2a48" stroke-width="2"/>
</svg>
<div class="abs hero-rule"></div>
<div class="abs stat" style="left:268px"><b>$40M+</b><small>MONEY RAISED</small></div>
<div class="abs stat" style="left:457px"><b>$125M+</b><small>ATTRIBUTED REVENUE</small></div>
<div class="abs stat" style="left:668px"><b>11</b><small>COMPANY EXITS</small></div>
<div class="abs stat" style="left:847px"><b>2</b><small>AWARDS WON</small></div>

<!-- expertise -->
<div class="deco" style="left:1044px;top:1099px;width:172px;height:172px;background:var(--ice)" role="img" aria-label="Soft decorative circle"></div>
<div class="photo" style="left:651px;top:764px;width:457px;height:427px;background:linear-gradient(160deg,#35b9e6,#2aa5d8)" role="img" aria-label="Portrait of a smiling young man in a denim shirt on a blue backdrop"></div>
<h2 class="abs sec-title" style="left:0;width:650px;text-align:center;top:964px">Area of expertise</h2>
<div class="abs underline" style="left:302px;top:1034px"></div>
<p class="abs lead" style="left:125px;top:1060px;width:400px">Help you build your network, introducing you to the right people in the right places.</p>

<svg class="abs" style="left:150px;top:1290px" width="900" height="240" fill="none" stroke="#3b4352" stroke-width="1.6">
  <circle cx="22" cy="22" r="17"/><ellipse cx="22" cy="22" rx="7" ry="17"/><line x1="5" y1="22" x2="39" y2="22"/>
  <rect x="334" y="6" width="26" height="18" rx="3"/><circle cx="338" cy="34" r="7"/><path d="M326 50 q12 -12 24 0"/>
  <circle cx="667" cy="28" r="11"/><path d="M650 20 v-14 M684 20 v-14 M646 10 l4 -6 4 6 M680 10 l4 -6 4 6"/>
  <path d="M4 195 l12 -10 10 6 12 -8 10 10 -12 12 z"/>
  <circle cx="345" cy="185" r="10"/><path d="M332 215 v-12 M345 215 v-16 M358 215 v-10"/>
  <circle cx="670" cy="200" r="8"/><circle cx="670" cy="200" r="17" stroke-dasharray="6 4"/>
</svg>
<div class="abs skill" style="left:211px;top:1291px"><h4>NETWORK<br>SUPPORT</h4><p>Help you build your network, introducing you to the right people in the right places.</p></div>
<div class="abs skill" style="left:534px;top:1291px"><h4>CONSULT ON<br>MARKETING</h4><p>Consult on marketing process, strategies and implementation across your startup.</p></div>
<div class="abs skill" style="left:857px;top:1291px"><h4>RAISING<br>CAPITAL</h4><p>Reach out to our extensive connections to raise vital capital for your startup.</p></div>
<div class="abs skill" style="left:211px;top:1473px"><h4>MERGERS &amp;<br>ACQUISTIONS</h4><p>Facilitate a smooth mergers and acquisition process for the expansion of your business.</p></div>
<div class="abs skill" style="left:534px;top:1473px"><h4>REVENUE<br>ACCELERATION</h4><p>Analyze your revenue streams, providing solutions for kickstarting your revenue.</p></div>
<div class="abs skill" style="left:857px;top:1473px"><h4>INTEGRATION &amp;<br>INCUBATION</h4><p>Providing training and guidance for startups looking to make their mark on the world.</p></div>

<!-- story -->
<div class="deco" style="left:-29px;top:2099px;width:172px;height:172px;background:var(--ice)" role="img" aria-label="Soft decorative circle"></div>
<section class="abs story"></section>
<div class="photo" style="left:89px;top:1778px;width:458px;height:426px;background:linear-gradient(135deg,#b9b9b9,#8f8f8f);box-shadow:0 20px 40px rgba(0,0,0,.15)" role="img" aria-label="Excited man in glasses holding a laptop against a grey wall"></div>
<div class="abs story-copy">
  <h2>Our story</h2>
  <p>Holvencrest Ventures is a venture capital studio firm based in Austin TX with a laser focus on raising solid capital for startups and helping businesses jumpstart their revenue.</p>
  <p>Founded in 2020 by investment expert Marcus Holven, Holvencrest Ventures combines proven experience in the venture capital field with a data-driven business analysis strategy to secure capital and reinforce revenue streams for startups and established businesses. Born from the idea that the best way to help founders thrive is to understand their strengths, their weaknesses, their ambitions and their needs - our specialists have been through the entire startup process themselves, and that experience forms our unique approach to business support.</p>
</div>
<div class="abs btn-white">LET'S WORK TOGETHER</div>

<!-- portfolio -->
<h2 class="abs sec-title" style="left:0;width:1200px;text-align:center;top:2389px">Our portfolio</h2>
<div class="abs underline" style="left:577px;top:2457px"></div>
<div class="abs grid">
  <div>Norvale</div><div>Quillby</div><div>tandra</div><div>fernlow</div><div style="font-size:16px">Keenpath</div>
  <div>Orbit Kinetics</div><div style="font-size:21px">urbanreach</div><div style="font-size:21px">Calvyra</div><div>brightlot</div><div style="font-size:18px;letter-spacing:3px;font-weight:600">TERRA LANE</div>
</div>
<svg class="abs" style="left:574px;top:2873px" width="52" height="16">
  <circle cx="8" cy="8" r="4.5" fill="none" stroke="#1c2a48" stroke-width="2"/>
  <circle cx="26" cy="8" r="4.5" fill="none" stroke="#9aa3b3" stroke-width="1.5"/>
  <circle cx="44" cy="8" r="4.5" fill="none" stroke="#1c2a48" stroke-width="2"/>
</svg>

<!-- approach -->
<section class="abs approach-bg"></section>
<div class="deco" style="left:1044px;top:3384px;width:172px;height:172px;background:var(--ice)" role="img" aria-label="Soft decorative circle"></div>
<div class="abs approach-copy">
  <h2>Our approach</h2>
  <p>We've built our approach to helping your startup thrive based around three key developmental pillars that guarantee results for our partners.</p>
  <p>First pillar is expertise. We've built our firm on a bank of insights, knowledge and proficiencies honed over years of working with the biggest names in venture capitalism – that experience forms the backbone of every project, every pitch and every investment.</p>
  <p>Second pillar is collaboration. We believe that the best partnerships start with a combined and cooperative approach that benefits all parties every step of the way. We'll always keep our partners up-to-date with our work using regular touchpoints and reports.</p>
  <p>Third and final pillar is trust. We know that our clients and our partners know their industry better than we do, so we trust their input and their ideas – pairing them up with our own business intelligence to guarantee success.</p>
</div>
<div class="photo" style="left:653px;top:3068px;width:458px;height:427px;background:linear-gradient(160deg,#9cbfd0,#86aec2)" role="img" aria-label="Bearded man in an orange t-shirt with arms crossed on a blue-grey backdrop"></div>

<!-- blog -->
<h2 class="abs sec-title" style="left:0;width:1200px;text-align:center;top:3667px">Latest blog</h2>
<article class="abs card" style="left:164px">
  <div class="thumb" style="background:linear-gradient(160deg,#3aa3b9,#2b8ea6)" role="img" aria-label="Young man working on a laptop against a teal backdrop"></div>
  <div class="body"><time>July 04, 2022</time><h3>Some blog heading goes here with des...</h3><p>Aenean sollicitudin lorem quis bibendum auctor nisi elit...</p></div>
</article>
<article class="abs card" style="left:460px">
  <div class="thumb" style="background:linear-gradient(160deg,#f0a4ad,#e48e99)" role="img" aria-label="Excited man holding a phone against a pink backdrop"></div>
  <div class="body"><time>July 04, 2022</time><h3>Some blog heading goes here with des...</h3><p>Aenean sollicitudin lorem quis bibendum auctor nisi elit...</p></div>
</article>
<article class="abs card" style="left:757px">
  <div class="thumb" style="background:linear-gradient(160deg,#f5b13c,#e99f2a)" role="img" aria-label="Man in glasses holding a laptop against an orange backdrop"></div>
  <div class="body"><time>July 04, 2022</time><h3>Some blog heading goes here with des...</h3><p>Aenean sollicitudin lorem quis bibendum auctor nisi elit...</p></div>
</article>

<!-- footer -->
<footer class="abs footer"></footer>
<div class="abs foot-brand">HOLVENCREST <span>VENTURES</span></div>
<div class="abs social" style="left:255px" aria-label="Social profile"></div>
<div class="abs social" style="left:321px" aria-label="Social profile"></div>
<div class="abs social" style="left:385px" aria-label="Social profile"></div>

<h3 class="abs form-title">Build with us</h3>
<span class="abs label" style="left:583px;top:4413px">NAME*</span>
<span class="abs label" style="left:819px;top:4413px">EMAIL*</span>
<div class="abs field" style="left:583px;top:4431px;width:227px;height:38px">Enter your name</div>
<div class="abs field" style="left:819px;top:4431px;width:228px;height:38px">Enter your email</div>
<span class="abs label" style="left:583px;top:4483px">PHONE*</span>
<div class="abs field" style="left:583px;top:4500px;width:464px;height:37px">Enter phone number</div>
<span class="abs label" style="left:583px;top:4551px">PHONE*</span>
<div class="abs field" style="left:583px;top:4568px;width:464px;height:118px;align-items:flex-start;padding-top:14px">Type your text...</div>
<div class="abs submit">SUBMIT NOW</div>
<svg class="abs" style="left:1017px;top:4718px" width="16" height="16" viewBox="0 0 16 16"><path d="M1 8 L15 1 L10 15 L8 9 Z" fill="#ffffff"/></svg>
<div class="abs foot-rule"></div>
<p class="abs copyright">COPYRIGHT © 2022 HOLVENCREST.COM</p>
<div class="abs to-top"></div>
<svg class="abs" style="left:1147px;top:4796px" width="16" height="16"><path d="M3 10 L8 5 L13 10" fill="none" stroke="#1c2a48" stroke-width="2"/></svg>

</body>
</html>
```